Bluefern Capital Counsel Needs a Letterhead

Tomi, we need a letterhead/banner for our blog, which is titled "Quiet Harbor Chronicle". The letterhead/banner should incorporate the enclosed banner image, logo, and the name of our blog ("Quiet Harbor Chronicle").

We would also like an alternative design that includes our picture. Here, we have two options that we would like to see.

In all, we would like to see 3 different designs: one banner without any pics; and two banner with two versions of our pictures.

The file size should be able to be resized for the space given to us at our website (http://bluefern-capital-counsel.com).

We also need the letterhead/banner by Friday, June 13. Thanks!!

```html
<!DOCTYPE html>
<html lang="en">
<head>
<meta charset="utf-8">
<title>Quiet Harbor Chronicle — Blog Banner</title>
<link rel="stylesheet" href="https://fonts.googleapis.com/css2?family=Cinzel:wght@500&display=swap">
<style>
  :root {
    --ink-black: #070707;
    --smoke-dark: #1c1c1c;
    --smoke-mid: #3a3a3a;
    --smoke-light: #676767;
    --title-gold: #b7b46e;
  }
  html, body {
    margin: 0;
    padding: 0;
    width: 1200px;
    height: 629px;
    overflow: hidden;
    background: var(--ink-black);
  }
  .banner {
    position: relative;
    width: 1200px;
    height: 629px;
    overflow: hidden;
  }
  .banner-photo {
    position: absolute;
    inset: 0;
    background:
      radial-gradient(ellipse 160px 70px at 1150px 260px, rgba(90,90,90,0.45), transparent 70%),
      radial-gradient(ellipse 120px 90px at 930px 140px, rgba(60,60,60,0.35), transparent 70%),
      radial-gradient(ellipse 140px 110px at 1080px 470px, rgba(55,55,55,0.35), transparent 70%),
      radial-gradient(ellipse 110px 80px at 760px 380px, rgba(45,45,45,0.3), transparent 70%),
      radial-gradient(ellipse 120px 90px at 420px 70px, rgba(40,40,40,0.3), transparent 70%),
      linear-gradient(to right,
        var(--smoke-light) 0px,
        #5c5c5c 170px,
        var(--smoke-mid) 225px,
        var(--smoke-dark) 265px,
        var(--ink-black) 330px,
        #0d0d0d 70%,
        #161616 100%);
  }
  .banner-title {
    position: absolute;
    left: 0;
    right: 0;
    top: 298px;
    margin: 0;
    padding-left: 44px;
    text-align: center;
    font-family: "Cinzel", "Trajan Pro", serif;
    font-weight: 500;
    font-size: 56px;
    line-height: 1;
    letter-spacing: 1px;
    color: var(--title-gold);
    font-variant: small-caps;
  }
</style>
</head>
<body>
  <header class="banner">
    <div class="banner-photo" role="img" aria-label="Dark, softly blurred photograph with a grey band of light on the left and faint out-of-focus shapes"></div>
    <h1 class="banner-title">Quiet Harbor Chronicle</h1>
  </header>
</body>
</html>
```